New Alcoholic Spiked Seltzer Line

We need a can design for a line of low calorie alcoholic seltzer. This product is a sparkling water and vodka drink with no sugar added in a slim 12 oz can.

This is a lighter, healthier, alternative to the sugary ready-to-drinks on the market. The product contains only 3 ingredients: Vodka, Water and Natural Flavors. It has only 100 calories but still has 5% alcohol, so you don't need to sacrifice alcohol to cut calories.

This product also does not contain any preservatives.

We want this design to communicate the following objectives to the consumer and in this order:

1. Appetizing product
2.Low calorie
3.Communicate the type of beverage (Spiked Seltzer)

The brand name of the product is VELKA.

The flavor of the product needed to be used for the design is Mango-Orange.

Comparable products are:

www.brisavelfizz.example/
https://www.tarnowbubble.example
https://quellrind.example/

The designs should not infringe or copy the creative directions of the products mentionned above. They are only given so that you can better understand the type of product we are developing.

Target Market(s)

Young Professional women between the ages of 25 and 44

Industry/Entity Type

Product

Colors

Designer to choose colors to be used in the design.

Requirements
Must have
• Design extendibility, meaning it can be adapted for other flavors.
• This is a new category in the market we are targeting, so consumers must easily be able to identify what type of product this is.

```html
<!DOCTYPE html>
<html lang="en">
<head>
<meta charset="utf-8">
<title>VELKA Spiked Seltzer – Mango Orange</title>
<link rel="stylesheet" href="https://fonts.googleapis.com/css2?family=Oswald:wght@400;500&family=Montserrat:wght@300;400&family=Space+Mono:wght@700&family=Great+Vibes&display=swap">
<style>
  :root{
    --backdrop:#e4e4e4;
    --label:#ffffff;
    --ink:#1c1c1c;
    --muted:#555555;
    --mango:#e8641c;
    --orange:#f2a93b;
    --orange-soft:#fbe1bd;
  }
  *{box-sizing:border-box;margin:0;padding:0}
  html,body{width:1200px;height:1200px;overflow:hidden;background:var(--backdrop)}
  .can-label{
    position:absolute;left:380px;top:70px;width:440px;height:1060px;
    background:var(--label);border-radius:6px;
    box-shadow:0 2px 10px rgba(0,0,0,.06);
    color:var(--ink);
  }
  .brand-name{
    position:absolute;left:0;right:0;top:330px;text-align:center;
    font-family:'Oswald',sans-serif;font-weight:500;font-size:150px;
    letter-spacing:6px;line-height:1;color:var(--ink);
  }
  .info-block{position:absolute;left:22px;right:22px;top:720px}
  .category-row{
    display:flex;align-items:stretch;border-top:2px solid var(--ink);border-bottom:2px solid var(--ink);
    height:46px;
  }
  .category{
    flex:1;display:flex;align-items:center;justify-content:center;
    font-family:'Montserrat',sans-serif;font-weight:400;font-size:15px;letter-spacing:7px;
    border-right:2px solid var(--ink);
  }
  .established{
    padding:0 12px;display:flex;align-items:center;
    font-family:'Oswald',sans-serif;font-size:22px;
  }
  .ingredients{
    text-align:center;font-family:'Montserrat',sans-serif;font-weight:300;font-size:20px;
    letter-spacing:3px;color:var(--muted);padding:12px 0 10px;
    border-bottom:3px dotted var(--ink);
  }
  .flavor-row{display:flex;align-items:center;height:130px;border-bottom:3px dotted var(--ink)}
  .abv{width:90px;text-align:center;border-right:2px solid var(--ink);padding-right:8px}
  .abv-figure{font-family:'Oswald',sans-serif;font-weight:500;font-size:56px;line-height:1}
  .abv-label{font-family:'Oswald',sans-serif;font-size:17px;color:var(--muted)}
  .fruit-placeholder{
    width:104px;height:104px;margin-left:24px;flex:none;border-radius:4px;
    background:radial-gradient(circle at 45% 50%, var(--orange-soft), var(--orange) 70%, var(--mango));
  }
  .flavor-name{
    flex:1;text-align:center;font-family:'Great Vibes',cursive;font-size:44px;line-height:.95;
  }
  .flavor-name .first{color:var(--mango);display:block}
  .flavor-name .second{color:var(--orange);display:block}
  .claims{
    text-align:center;font-family:'Montserrat',sans-serif;font-weight:300;font-size:15px;
    color:var(--muted);padding:10px 0 8px;border-bottom:2px solid var(--ink);
  }
  .tagline{
    text-align:center;font-family:'Space Mono',monospace;font-weight:700;font-size:13.5px;
    padding:10px 0;border-bottom:2px solid var(--ink);white-space:nowrap;
  }
</style>
</head>
<body>
  <main class="can-label">
    <h1 class="brand-name">VELKA</h1>
    <section class="info-block">
      <div class="category-row">
        <div class="category">Spiked Seltzer</div>
        <div class="established">est. MMXVII Canada</div>
      </div>
      <p class="ingredients">Vodka mixed with water</p>
      <div class="flavor-row">
        <div class="abv">
          <div class="abv-figure">5%</div>
          <div class="abv-label">Alc. Vol.</div>
        </div>
        <div class="fruit-placeholder" role="img" aria-label="Mango orange fruit icon, split ring in orange tones with a small leaf"></div>
        <p class="flavor-name"><span class="first">Mango</span><span class="second">Orange</span></p>
      </div>
      <p class="claims">100% calories / No preservatives / Natural Flavor</p>
      <p class="tagline">unlike something you'd expact to find in a can</p>
    </section>
  </main>
</body>
</html>
```